Psychotherapist's business card

I need a business card design for a psychotherapist. I expect business card to have "light" design. By this I mean that it can somehow translate easiness, serenity. Maybe pastel colours can help you here. I have attached some pictures from Greece. Perhaps they can inspire you to combine colours and to achieve that "light" design.
Updates

Pls, don't use any free samples you may find on business card generators. It looks too simple, uncreative and waste of time! READ size and colour requirements! I don't want to see any shapes like rings, triangles etc.

Contact Information for Business Card

Size: 65mmX60mm

Name - Вячеслав Мирошенко

Психолог
+7(916)482-30-67
miroshenko.com

I suppose that thin font can look good but it's up to you

Requirements
Must have
• size requirements
Nice to have
• pastel colours
• thin font
Should not have
• black and dark colours
• lines, free design samples used from other web-sites

```html
<!DOCTYPE html>
<html lang="ru">
<head>
<meta charset="utf-8">
<title>Вячеслав Мирошенко — Психолог</title>
<link rel="stylesheet" href="https://fonts.googleapis.com/css2?family=Open+Sans:wght@300;400;700&display=swap">
<style>
  :root {
    --backdrop: #e9ebf0;
    --card-top: #cdd5ec;
    --card-bottom: #9fa6b8;
    --bar-light: #f4f3ef;
    --bar-shade: #c9c8c2;
    --name-ink: #e4e7ef;
    --role-ink: #1c1e24;
    --phone-ink: #d3d7e2;
    --web-ink: #15161a;
  }
  html, body {
    margin: 0;
    width: 1200px;
    height: 873px;
    overflow: hidden;
    background: var(--backdrop);
    font-family: "Open Sans", sans-serif;
  }
  .stage {
    position: relative;
    width: 1200px;
    height: 873px;
  }
  .business-card {
    position: absolute;
    left: 340px;
    top: 196px;
    width: 520px;
    height: 480px;
    background: linear-gradient(160deg, var(--card-top) 0%, #b8bfd6 55%, var(--card-bottom) 100%);
    box-shadow: 0 6px 22px rgba(40, 44, 60, 0.18);
  }
  .accent-bar {
    position: absolute;
    left: 252px;
    width: 14px;
    background: linear-gradient(90deg, var(--bar-light), var(--bar-shade));
  }
  .accent-bar--top { top: 0; height: 168px; }
  .accent-bar--bottom { top: 322px; height: 158px; }
  .card-details {
    position: absolute;
    left: 0;
    right: 0;
    top: 176px;
    text-align: center;
  }
  .person-name {
    margin: 0;
    font-weight: 300;
    font-size: 27px;
    line-height: 1.1;
    color: var(--name-ink);
  }
  .person-role {
    margin: 2px 0 0;
    font-weight: 400;
    font-size: 27px;
    line-height: 1.1;
    color: var(--role-ink);
  }
  .contact-phone {
    margin: 18px 0 0;
    font-weight: 300;
    font-size: 19px;
    color: var(--phone-ink);
    display: flex;
    justify-content: center;
    align-items: center;
    gap: 10px;
  }
  .contact-phone svg { width: 18px; height: 16px; }
  .contact-web {
    margin: 10px 0 0;
    font-weight: 700;
    font-size: 20px;
    color: var(--web-ink);
  }
</style>
</head>
<body>
<main class="stage">
  <section class="business-card" aria-label="Визитная карточка психолога">
    <div class="accent-bar accent-bar--top"></div>
    <div class="card-details">
      <h1 class="person-name">Вячеслав Мирошенко</h1>
      <p class="person-role">Психолог</p>
      <p class="contact-phone">
        <svg viewBox="0 0 18 16" aria-hidden="true">
          <path d="M1 5 C1 2 5 1 9 1 C13 1 17 2 17 5 L17 6 L13 6 L12.5 4 L5.5 4 L5 6 L1 6 Z" fill="var(--role-ink)"/>
          <path d="M5 7 L13 7 L16 15 L2 15 Z" fill="var(--role-ink)"/>
          <circle cx="9" cy="11" r="2" fill="var(--card-top)"/>
        </svg>
        <span>+7(916)482-30-67</span>
      </p>
      <p class="contact-web">www.miroshenko.com</p>
    </div>
    <div class="accent-bar accent-bar--bottom"></div>
  </section>
</main>
</body>
</html>
```